Book Cover "Venice"

Creation of a cover (14 x 20.5 cm + bleed area) for a book:
Image: “BrumeVerte” (Tiff joined)
AUTHOR: Corinne Valmer
TITLE: The murmurs of Lorient
PUBLISHER: Editions Pluvane (AT THE BOTTOM OF THE COVER)

Target Market(s)

Readers of romantic novels

Industry/Entity Type

Book

```html
<!DOCTYPE html>
<html lang="en">
<head>
<meta charset="utf-8">
<title>The Murmurs of Lorient — Book Cover</title>
<link rel="stylesheet" href="https://fonts.googleapis.com/css2?family=Cinzel:wght@400&family=Great+Vibes&display=swap">
<style>
  :root {
    --page-bg: #ffffff;
    --sky-top: #7d1420;
    --sky-upper: #b01d22;
    --sky-mid: #d32d1f;
    --sky-glow: #e6441f;
    --sky-low: #c8281a;
    --silhouette: #1e0808;
    --night: #050303;
    --ink-light: #ffffff;
  }
  * { box-sizing: border-box; margin: 0; padding: 0; }
  html, body {
    width: 1200px;
    height: 1200px;
    overflow: hidden;
    background: var(--page-bg);
  }
  .stage {
    position: relative;
    width: 1200px;
    height: 1200px;
  }
  .book-cover {
    position: absolute;
    left: 217px;
    top: 40px;
    width: 766px;
    height: 1120px;
    overflow: hidden;
  }
  .sky-photo {
    position: absolute;
    inset: 0;
    background: linear-gradient(180deg,
      var(--sky-top) 0%,
      var(--sky-upper) 16%,
      var(--sky-mid) 36%,
      var(--sky-glow) 52%,
      var(--sky-low) 66%,
      var(--sky-low) 100%);
  }
  .skyline-photo {
    position: absolute;
    left: 0;
    right: 0;
    top: 620px;
    bottom: 0;
    background:
      radial-gradient(ellipse 40% 30% at 68% 35%, rgba(255, 190, 120, 0.22), transparent 70%),
      linear-gradient(180deg,
        rgba(30, 8, 8, 0) 0%,
        rgba(30, 8, 8, 0.75) 18%,
        var(--silhouette) 40%,
        var(--night) 78%,
        var(--night) 100%);
  }
  .author {
    position: absolute;
    top: 70px;
    left: 0;
    width: 100%;
    text-align: center;
    font-family: "Cinzel", serif;
    font-weight: 400;
    font-size: 31px;
    line-height: 1;
    letter-spacing: 0.1em;
    color: var(--ink-light);
  }
  .title {
    position: absolute;
    inset: 0;
    font-family: "Great Vibes", cursive;
    font-weight: 400;
    color: var(--ink-light);
    line-height: 1;
  }
  .title-line {
    position: absolute;
    left: 0;
    width: 100%;
    text-align: center;
    white-space: nowrap;
  }
  .title-the {
    top: 172px;
    font-size: 140px;
    padding-left: 30px;
  }
  .title-main {
    top: 248px;
    font-size: 180px;
  }
  .title-place {
    top: 440px;
    font-size: 186px;
    padding-left: 50px;
  }
  .title-of {
    font-size: 70px;
    margin-right: 6px;
  }
  .publisher {
    position: absolute;
    top: 1052px;
    left: 0;
    width: 100%;
    text-align: center;
    font-family: "Cinzel", serif;
    font-weight: 400;
    font-size: 22px;
    line-height: 1;
    letter-spacing: 0.1em;
    color: var(--ink-light);
  }
</style>
</head>
<body>
  <main class="stage">
    <section class="book-cover">
      <div class="sky-photo" role="img" aria-label="Photograph: blazing red and orange sunset sky with streaked clouds"></div>
      <div class="skyline-photo" role="img" aria-label="Photograph: dark silhouette of a harbour city skyline with domed church towers and glowing street lanterns in the foreground"></div>
      <p class="author">CORINNE VALMER</p>
      <h1 class="title">
        <span class="title-line title-the">The</span>
        <span class="title-line title-main">Murmurs</span>
        <span class="title-line title-place"><span class="title-of">of</span>Lorient</span>
      </h1>
      <p class="publisher">EDITIONS PLUVANE</p>
    </section>
  </main>
</body>
</html>
```